Stationery Design Project

We need a stationery design to change our look to a more corporate design. My company has been established since 1989 and over that time has changed from your average sign company to doing more Corporate re branding projects and have some multi National clients.
Our website is currently being redesigned so we need a new logo and business cards etc. to compliment it.
I have 2 graphic designers employed but i want on outsiders opinion and a totally independant view point.
Updates
Hi Designers
We are predominantely a sign manufacturing company that manufacturers every type of sign you can imagine. However the majoprity of our work is digital graphics. Our claim to faim is that we wrap the Harbour Skytrams and Glidetrams which everyone seems to know in Sydney.We also do all sorts of Large format digital printing, vehicle wraps,vinyl signage,LED & Neon Illuminated signage,CNC Routing all materials,Laser cutting and Engraving, Architectural signage, Cut Out letters and Screenprinting.
Aswell as this we totally re-brand companies with internal wall graphics reception signage way finding signage and the like.We are a medium size company that has been trading since 1989 and has some very large reputable clients.
Our Company name is Brightmark Pty Ltd but like to have Signage and Graphics in our stationery.
Our details are as follows T: 9381 5027 F: 9381 5063 Unit 4, 22 Quarry Lane.Pine Flats. NSW 2163 email mail@brightmarkexample.com our current website is being re-designed www.brightmarkexample.com
The design and colour scheme i would like is quite simple with a corporate feel and blue, grey & magenta are colours that seem to suit but am open to most suggestions just looking for clean lines.
Hopefully this is enough information if you require any more please ask.
Regards Neil Barrowby
We are looking to simplify our LOGO not too concerned yet about layout of stationery items that we can easily work on later. I want to get a new logo that we can work with before we return to work on the 16th January so please concentrate on just the logo for now.
We would like to have Signs & Graphics somewhere in the name even though our registered name is Brightmark Pty Ltd. Brightmark is one word, i want it to be quite a bold font with no seriffs.The bright blue and grey colours are favourites so far with maybe a little magenta added later. Would like to have a Logo that is totally seperate and then the Brightmark P/L Signs & graphics as a secondary item just to let people know what Brightmark do as the name obviously does not say what we are about.
Also we need to consider how we can put logo on T-shirts work shirts and company vehicles.
We do not need CD cover or envelopes but letterheads and business cards.
Industry/Entity Type
Business
Look and feel
Each slider illustrates characteristics of the customer's brand and the style your logo design should communicate.

```html
<!DOCTYPE html>
<html lang="en">
<head>
<meta charset="utf-8">
<title>Brightmark business card</title>
<link rel="stylesheet" href="https://fonts.googleapis.com/css2?family=Source+Sans+3:wght@300;400;600&display=swap">
<style>
  :root {
    --backdrop: #1b1b1b;
    --card: #ffffff;
    --card-shade: #e6e6e6;
    --ink: #222222;
    --ink-soft: #555555;
    --brand-blue: #0a86b2;
    --brand-blue-light: #2aa6c8;
    --brand-magenta: #ec0a85;
    --brand-magenta-light: #f55fab;
    --ring-grey: #666666;
  }
  * { box-sizing: border-box; margin: 0; padding: 0; }
  html, body {
    width: 1200px; height: 960px; overflow: hidden;
    background: var(--backdrop);
    font-family: "Source Sans 3", Arial, sans-serif;
  }
  .card {
    position: absolute; left: 254px;
    width: 634px; height: 362px;
    border-radius: 23px; overflow: hidden;
    background: linear-gradient(to bottom, var(--card) 70%, var(--card-shade) 100%);
  }
  .card--front { top: 97px; }
  .card--back  { top: 482px; background: linear-gradient(to bottom, var(--card) 60%, var(--card-shade) 100%); }
  .card__decor { position: absolute; inset: 0; }
  .brand {
    position: absolute; display: flex; align-items: center; gap: 14px;
  }
  .brand__dot {
    width: 72px; height: 72px; border-radius: 50%;
    background: var(--brand-blue);
  }
  .brand__name {
    font-size: 43px; font-weight: 400; color: var(--ink); line-height: 1;
  }
  .card--front .brand { left: 302px; top: 257px; }
  .card--back .brand { left: 33px; top: 32px; }
  .contact { position: absolute; left: 36px; top: 140px; color: var(--ink); }
  .contact__name { font-size: 24px; font-weight: 600; color: var(--brand-blue); line-height: 1.1; }
  .contact__role { font-size: 16px; font-weight: 300; color: var(--ink-soft); margin-top: 2px; }
  .contact__address { font-size: 16px; font-weight: 300; line-height: 21px; margin-top: 24px; }
  .contact__list { list-style: none; margin-top: 10px; font-size: 16px; font-weight: 300; }
  .contact__list li { display: flex; align-items: center; height: 22.5px; }
  .contact__list svg { width: 14px; height: 14px; margin: 0 14px 0 8px; fill: var(--brand-blue); }
</style>
</head>
<body>

<section class="card card--front">
  <svg class="card__decor" width="634" height="362" viewBox="0 0 634 362" aria-hidden="true">
    <defs>
      <linearGradient id="blue-fill" x1="0" y1="0" x2="0" y2="1">
        <stop offset="0" stop-color="var(--brand-blue-light)"/>
        <stop offset="0.5" stop-color="var(--brand-blue)"/>
      </linearGradient>
    </defs>
    <circle cx="76" cy="175" r="172" fill="url(#blue-fill)"/>
  </svg>
  <div class="brand">
    <span class="brand__dot"></span>
    <span class="brand__name">Brightmark</span>
  </div>
</section>

<section class="card card--back">
  <svg class="card__decor" width="634" height="362" viewBox="0 0 634 362" aria-hidden="true">
    <defs>
      <linearGradient id="magenta-fill" x1="0" y1="0" x2="0" y2="1">
        <stop offset="0" stop-color="var(--brand-magenta-light)"/>
        <stop offset="0.7" stop-color="var(--brand-magenta)"/>
      </linearGradient>
    </defs>
    <circle cx="497" cy="225" r="172" fill="url(#magenta-fill)"/>
  </svg>
  <div class="brand">
    <span class="brand__dot"></span>
    <span class="brand__name">Brightmark</span>
  </div>
  <div class="contact">
    <p class="contact__name">Marcus Ellery</p>
    <p class="contact__role">Marketing Manager</p>
    <p class="contact__address">22 Quarry Lane<br>Pine Flats. NSW 2163</p>
    <ul class="contact__list">
      <li><svg viewBox="0 0 14 14"><path d="M1 5c0-2 2-3 6-3s6 1 6 3v1h-3V5H4v1H1z M3 7h8l1 5H2z"/></svg>9381 5027</li>
      <li><svg viewBox="0 0 14 14"><path d="M3 1h8v4H3z M1 6h12v5H1z M3 9h8v4H3z" /></svg>9381 5063 Unit 4</li>
      <li><svg viewBox="0 0 14 14"><path d="M1 3h12v8H1z M2 4l5 4 5-4v-0.5H2z" fill-rule="evenodd"/></svg>marcus@brightmarkexample.com</li>
      <li><svg viewBox="0 0 14 14"><circle cx="7" cy="7" r="6"/></svg>www.brightmarkexample.com</li>
    </ul>
  </div>
</section>

</body>
</html>
```